Tallant Family Adoption Fundraiser

The sole purpose of this card is to tell people about the fundraiser and direct them to the website that will allow them to participate.  No other contact information is needed.
Since our approach is through personal networking, this card is our sole marketing piece and needs to be effective.  We will use an image of the card for the email & Facebook outreaches we will do.  We have a very limited budget (thus the fundraiser).
We will need a quantity of 2,000 cards.  We dont need to pay for high gloss or metalic finishes, but we were thinking we probably would want a folded business card to give us more real estate to work with.
About the fundraiser (will help you understand the content needed):  Our family is adopting a young girl from Colombia, South America.  We need to raise about $15,000 to bring her home.  This fundraiser is something called a "Duck Race".  People will go to our website and 'purchase' ducks for the race.  For each duck, there will be a rubber duck in the 'race' with their own unique number on it.  On the day of the race, all of the ducks are dumped into a river.  The first ones to cross the finish line down stream is the winner.  The more ducks people put in the race in their name, the more chances they have to win the cash prizes.  We will video the race, and show it on our website.  The idea was to make this an effective and low maintenance fundraiser - nobody has to attend an event - people dont even need to know us, they only need to want to have a chance at the cash prize.  With that being said, here are some ideas of content:
- title:  "The Splendid Paddle Dash"
- "Win 1 of 3 cash prizes totalling $1,000
- www.Welcoming Little Sparrow Back.example
- The Tallant family is adopting a young girl from Colombia, South America, and needs your help to bring her home.
-  We could include a picture of her.
-  We have an icon of a Duck holding a Colombian flag - this is an icon our son created and must be used as the focal point.  We want our existing kids (3 boys) to be part of this and our son Corwin love computer animation and drawing - he created the icon.
-  People can sponsor a duck in the race or simply make their own, individual donation through the website.
-  We are using duck puns like crazy - we will even have a duck pun contest and the winners get free additional ducks in the race.
-  We want our network to be able to use these cards to get others to participate because of the cause - even if they do not know us.  That is why we thought the folded cards would be good because we would have space to put our testimony.  If cost-prohibitive, then we will settle for a 2-sided card.
We are open to suggestions, but time is absolutely of the essence.  We just got approved by Colombia, but we only have 2 weeks left to network with folks in our schools before they are done for the year.  We need a very quick turn-around.

Updates
Due to a browser issue, the icon was not uploaded in my brief.  They are in the process of manually adding it to my brief now and should be available shortly. Thank you for your help.

Target Market(s)
Potential donors/sponsors
Industry/Entity Type
Real Estate
Contact Information for Business Card
www.WelcomingLittleSparrowBack.example
Requirements
Must have
- Catchy but simple exterior to make people want to see the interior of a folded business card.

```html
<!DOCTYPE html>
<html lang="en">
<head>
<meta charset="utf-8">
<title>The Splendid Paddle Dash – Fundraiser Card</title>
<link href="https://fonts.googleapis.com/css2?family=Delius&family=Questrial&display=swap" rel="stylesheet">
<style>
  :root {
    --page-bg: #efece6;
    --card-white: #ffffff;
    --lime: #c3cf21;
    --lime-dark: #aab51a;
    --title-grey: #7d7d7d;
    --text-light: #ffffff;
    --flag-yellow: #f4d21c;
    --flag-blue: #2a3f9a;
    --flag-red: #d32b2b;
    --shadow: rgba(0,0,0,0.18);
  }
  * { box-sizing: border-box; margin: 0; padding: 0; }
  html, body { width: 1200px; height: 1000px; overflow: hidden; }
  body { background: var(--page-bg); position: relative; font-family: "Questrial", sans-serif; }

  .card {
    position: absolute;
    display: flex;
    border-radius: 22px;
    overflow: hidden;
    box-shadow: 0 6px 18px var(--shadow);
  }
  .panel { position: relative; height: 100%; }

  /* Outside of the folded card */
  .card--outside { left: 60px; top: 130px; width: 520px; height: 290px; }
  .card--outside .panel--left { width: 260px; background: var(--card-white); }
  .card--outside .panel--right { width: 260px; background: var(--lime); }

  .title-script {
    font-family: "Delius", cursive;
    color: var(--title-grey);
    font-size: 34px;
    position: absolute;
  }
  .title-script--light { color: var(--text-light); }
  .card--outside .title-script { left: 36px; bottom: 86px; }
  .card--outside .title-script--light { left: 40px; top: 80px; }

  /* Inside of the folded card */
  .card--inside { left: 620px; top: 130px; width: 520px; height: 290px; }
  .card--inside .panel--left { width: 380px; background: var(--card-white); border-right: 1px solid #d9d3cc; }
  .card--inside .panel--right { width: 140px; background: var(--card-white); }
  .card--inside .title-script { left: 30px; bottom: 70px; }

  .mascot {
    position: absolute;
    right: 26px; top: 40px;
    width: 150px; height: 120px;
    border-radius: 12px;
    background: linear-gradient(180deg, var(--flag-yellow) 0 50%, var(--flag-blue) 50% 75%, var(--flag-red) 75% 100%);
  }

  .prize-text {
    position: absolute;
    left: 50%; top: 50%;
    width: 250px;
    transform: translate(-50%, -50%) rotate(90deg);
    color: var(--lime);
    font-family: "Questrial", sans-serif;
    font-weight: 700;
    font-size: 19px;
    line-height: 1.25;
    text-align: center;
  }

  /* Back panel */
  .card--back {
    left: 93px; top: 660px; width: 703px; height: 325px;
    background: var(--lime);
  }
  .card--back .panel--title { width: 222px; border-right: 2px solid var(--text-light); }
  .card--back .title-script { left: 24px; top: 138px; font-size: 32px; }
  .card--back .panel--story { flex: 1; }
  .story {
    position: absolute; left: 0; right: 0; top: 100px;
    text-align: center;
    color: var(--text-light);
    font-size: 19px;
    line-height: 1.38;
  }
  .web-address {
    position: absolute; left: 0; right: 0; top: 254px;
    text-align: center;
    color: var(--text-light);
    font-weight: 700;
    font-size: 18px;
  }
</style>
</head>
<body>

  <section class="card card--outside" aria-label="Card outside">
    <div class="panel panel--left">
      <span class="title-script">The Splendid</span>
    </div>
    <div class="panel panel--right">
      <span class="title-script title-script--light">Paddle Dash</span>
    </div>
  </section>

  <section class="card card--inside" aria-label="Card inside">
    <div class="panel panel--left">
      <div class="mascot" role="img" aria-label="Child-drawn duck mascot in sunglasses holding a Colombian flag"></div>
      <span class="title-script">The Splendid</span>
    </div>
    <div class="panel panel--right">
      <p class="prize-text">Win 1 of 3 cash prizes<br>totalling $1,000</p>
    </div>
  </section>

  <section class="card card--back" aria-label="Card back">
    <div class="panel panel--title">
      <span class="title-script title-script--light">Paddle Dash</span>
    </div>
    <div class="panel panel--story">
      <p class="story">The Tallant family is adopting a young girl<br>from Colombia, South America,<br>and needs your help to bring her home</p>
      <p class="web-address">www.Welcoming Little Sparrow Back.example</p>
    </div>
  </section>

</body>
</html>
```